Wealth Education Business Needs Sharp Business Card Design

We need a business card design for a recently launched investor education business called Harbor Crest.

The final design should promote security, empowerment, self improvement and financial gain. The card will ideally promote the stature of the business.

For more information and colours please visit harborcrest.com.au

Target Market(s)

Corporate executives and high net worth individuals

Industry/Entity Type

Education

Contact Information for Business Card

Name
Position
Contact Address
Phone
Mobile
Email
Website

```html
<!DOCTYPE html>
<html lang="en">
<head>
<meta charset="utf-8">
<title>Harbor Crest — Business Card</title>
<link rel="stylesheet" href="https://fonts.googleapis.com/css2?family=Open+Sans:wght@400;600;700&display=swap">
<style>
  :root {
    --backdrop: #0b5f88;
    --card-dark: #42403e;
    --card-light: #ffffff;
    --ink: #3d3d3d;
    --brand-teal: #1a9a9c;
    --white: #ffffff;
  }
  * { margin: 0; padding: 0; box-sizing: border-box; }
  html, body {
    width: 1200px;
    height: 1000px;
    overflow: hidden;
  }
  body {
    background: var(--backdrop);
    font-family: "Open Sans", Arial, sans-serif;
    position: relative;
  }
  .card {
    position: absolute;
    left: 302px;
    width: 595px;
    height: 331px;
  }
  .card-front {
    top: 146px;
    background: var(--card-dark);
    display: flex;
    align-items: center;
    justify-content: center;
  }
  .card-front .wordmark {
    color: var(--white);
    font-weight: 600;
    font-size: 46px;
    letter-spacing: 0.14em;
    text-transform: uppercase;
    margin-top: -4px;
  }
  .card-back {
    top: 521px;
    background: var(--card-light);
    color: var(--ink);
  }
  .holder {
    position: absolute;
    left: 30px;
    top: 40px;
    font-size: 15px;
    line-height: 22px;
  }
  .holder .role { font-weight: 700; }
  .card-back .wordmark {
    position: absolute;
    right: 28px;
    top: 44px;
    color: var(--brand-teal);
    font-weight: 600;
    font-size: 27px;
    letter-spacing: 0.12em;
    text-transform: uppercase;
  }
  .contact-lines {
    position: absolute;
    left: 30px;
    top: 205px;
    font-size: 15px;
    line-height: 23px;
    list-style: none;
  }
  .contact-lines .phone + .phone { margin-top: 4px; }
  .contact-lines .address { margin-top: 4px; }
  .web-lines {
    position: absolute;
    right: 27px;
    top: 258px;
    font-size: 15px;
    line-height: 23px;
    text-align: right;
    list-style: none;
  }
</style>
</head>
<body>
  <section class="card card-front" aria-label="Card front">
    <div class="wordmark">Harbor Crest</div>
  </section>

  <section class="card card-back" aria-label="Card back">
    <div class="holder">
      <p class="name">Daniel Marsh</p>
      <p class="role">Manager</p>
    </div>
    <div class="wordmark">Harbor Crest</div>
    <ul class="contact-lines">
      <li class="phone">Tel: 0088 765432100</li>
      <li class="phone">Mob: 0088 765432100</li>
      <li class="address">Addr: 42 Example Lane<br>P.O. Box 55120</li>
    </ul>
    <ul class="web-lines">
      <li>info@harborcrest.com.au</li>
      <li>www.harborcrest.com.au</li>
    </ul>
  </section>
</body>
</html>
```